Business Card

I need a cool business card for Quill Films. You created logo for me so I'm thinking of using you for my business card. I want something simple, clean, artsy, but yet catchy to eye. I was thinking logo on one side and the information on the other. On teh phone, web, email, fb, and vimeo it would be cool to have the icons to identify each one. I would need these business cards formatted for prenta mart. If you have any recommendations for the card I'm fine with that. I might have to much information not sure.

Logo on one side

Dorn Vallick
Owner/Film Director
phone: 555.207.6183
web: quillfilms.example
email: dorn@quillfilms.example
FB: friendspage.example/quillfilmsLA
Vimeo: clipvault.example/user51093264

The other design I need is:
Marlo Pennick
Film Director/Editing
phone: 555.730.9164
web: quillfilms.example
email: marlo@quillfilms.example

Thanks

```html
<!DOCTYPE html>
<html lang="en">
<head>
<meta charset="utf-8">
<title>Quill Films — Business Card</title>
<link rel="stylesheet" href="https://fonts.googleapis.com/css2?family=Jost:wght@400;500;600&display=swap">
<style>
  :root {
    --brand-red: #d6182b;
    --ink: #1b1b1b;
    --ink-soft: #3a3a3a;
    --blush: #f6d3d7;
    --card-white: #ffffff;
    --card-grey: #d9d9d9;
    --backdrop: #e9e7e3;
    --social-blue: #2d6cb5;
    --social-teal: #1aa7d9;
  }
  * { box-sizing: border-box; margin: 0; padding: 0; }
  html, body {
    width: 1200px; height: 871px; overflow: hidden;
    background: var(--backdrop);
    font-family: "Jost", "Helvetica Neue", Arial, sans-serif;
  }
  .stage { position: relative; width: 1200px; height: 871px; }

  .card {
    position: absolute;
    width: 580px; height: 332px;
    border-radius: 2px;
    box-shadow: 0 10px 24px rgba(0,0,0,.22);
    overflow: hidden;
  }
  .card--front {
    left: 70px; top: 80px;
    background: linear-gradient(160deg, var(--card-white) 0%, #efefef 45%, var(--card-grey) 100%);
    display: flex; align-items: center; justify-content: center;
  }
  .card--back {
    left: 550px; top: 460px;
    background: linear-gradient(200deg, #ececec 0%, var(--card-white) 55%, var(--card-white) 100%);
  }

  .wordmark {
    display: flex; align-items: center; gap: 14px;
    color: var(--brand-red);
    font-weight: 600;
    letter-spacing: -0.5px;
    white-space: nowrap;
  }
  .wordmark__dot {
    border-radius: 50%;
    background: var(--brand-red);
    flex: none;
  }
  .card--front .wordmark { font-size: 64px; }
  .card--front .wordmark__dot { width: 46px; height: 46px; }

  .back__decor {
    position: absolute;
    left: 200px; top: -40px;
    width: 250px; height: 250px;
    border-radius: 50%;
    background: var(--blush);
    opacity: .55;
  }
  .card--back .wordmark {
    position: absolute; left: 38px; top: 92px;
    font-size: 40px;
  }
  .card--back .wordmark__dot { width: 28px; height: 28px; }

  .person {
    position: absolute; right: 34px; top: 112px;
    text-align: right;
  }
  .person__name {
    font-weight: 600; font-size: 17px; color: var(--ink);
    letter-spacing: .3px;
  }
  .person__role {
    font-size: 12.5px; color: var(--ink-soft); margin-top: 2px;
  }

  .contact {
    position: absolute; right: 30px; top: 186px;
    list-style: none;
  }
  .contact__item {
    display: flex; align-items: center; justify-content: flex-end;
    gap: 26px;
    font-size: 12px; color: var(--ink-soft);
    height: 20px;
  }
  .contact__icon { width: 12px; height: 12px; flex: none; }
  .contact__icon--social { border-radius: 2px; width: 10px; height: 10px; margin: 0 1px; }
  .contact__icon--friends { background: var(--social-blue); }
  .contact__icon--clips { background: var(--social-teal); }
</style>
</head>
<body>
<main class="stage">

  <section class="card card--front" aria-label="Card front">
    <div class="wordmark"><span class="wordmark__dot"></span>Quill Films</div>
  </section>

  <section class="card card--back" aria-label="Card back">
    <div class="back__decor" aria-hidden="true"></div>
    <div class="wordmark"><span class="wordmark__dot"></span>Quill Films</div>

    <div class="person">
      <p class="person__name">Dorn Vallick</p>
      <p class="person__role">Owner/Film Director</p>
    </div>

    <ul class="contact">
      <li class="contact__item">555.207.6183
        <svg class="contact__icon" viewBox="0 0 12 12" aria-label="phone"><path d="M1 4 Q6 0 11 4 L9.5 5.5 L8 4.5 L4 4.5 L2.5 5.5 Z M3 6 H9 L10 11 H2 Z" fill="#333"/></svg>
      </li>
      <li class="contact__item">dorn@quillfilms.example
        <svg class="contact__icon" viewBox="0 0 12 12" aria-label="email"><rect x="0.8" y="2.5" width="10.4" height="7" fill="none" stroke="#333" stroke-width="1.1"/><path d="M1 3 L6 7 L11 3" fill="none" stroke="#333" stroke-width="1.1"/></svg>
      </li>
      <li class="contact__item">quillfilms.example
        <svg class="contact__icon" viewBox="0 0 12 12" aria-label="web"><circle cx="6" cy="6" r="5" fill="none" stroke="#333" stroke-width="1.1"/><ellipse cx="6" cy="6" rx="2.2" ry="5" fill="none" stroke="#333" stroke-width=".9"/><path d="M1 6 H11" stroke="#333" stroke-width=".9"/></svg>
      </li>
      <li class="contact__item">friendspage.example/quillfilmsLA
        <span class="contact__icon contact__icon--social contact__icon--friends" aria-label="social page"></span>
      </li>
      <li class="contact__item">clipvault.example/user51093264
        <span class="contact__icon contact__icon--social contact__icon--clips" aria-label="video channel"></span>
      </li>
    </ul>
  </section>

</main>
</body>
</html>
```